Quiet Hollow Journals - Book Covers - Ebook, Paperback, Hardcover

Title would be:
Quiet Hollow Journals
Subtitle: 9 Simple Steps Including, Site Selection, Pollination and Fertilization, Pruning, Small Spaces, Pest Control, Tropical Fruit Trees, and Berries
Author: Marguerite Olundvale
I would like the designer to have a couple of beautiful pictures on the cover. Please make it unique.
This would be posted on Brindlo so please use specifications for book covers on Brindlo
Back Cover should read:
Quiet Hollow Journals
9 Simple Steps Including, Site Selection, Pollination and Fertilization, Pruning, Small Spaces, Pest Control, Tropical Fruit Trees, and Berries
Marguerite Olundvale
How to grow a thriving orchard and reap a bountiful harvest in less than a year – in both urban and non-urban settings
Fruit trees are fun to grow and will reward you with years of fresh, juicy homegrown produce.
However, the process can be excruciating, especially if you don’t know the best varieties to grow or how to control pests and diseases.
With a little planning and guidance, you will soon be biting into mellow fruits from trees in your backyard – including cherries, plums, pears, apples, and more.
All you need is to learn how to care for the trees, which you will find inside.
In Quiet Hollow Journals, you’ll discover:
● How to pick the right fruit tree varieties for your growing zone and needs to ensure the plants don’t die
● How to effectively plan and prepare the planting site to lay a good foundation for your incoming trees
● How to choose the right irrigation system for your orchard and keep your fruit trees nourished all year long
● Examples of fruit garden plans for different regions – including a guide to help you design your small backyard space
● How to plant fruits to ensure proper pollination, fertilization, and flourishing growth of your produce
● Different fruit tree propagation methods with step-by-step instructions to help you grow your trees without spending money on costly grafts
● When and how to harvest fruits to ensure you collect them at their best and prevent wasting your hard work
● How to boost fruit production, encourage growth, and protect your trees from dangerous diseases
● How to look after fruit trees during all seasons, practice organic farming, and control pests in your garden
And much more…
It’s time to grow your mini-orchard and bask in years of harvest and sweetness from your labor.
Discover how you can have a thriving orchard and a bountiful fruit harvest.
Updates
Hello all Designers,
Please include this on the back cover as I forgot to include it in my main project:
Back Cover to read:
Quiet Hollow Journals
Marguerite Olundvale
And much more…
Target Market(s)
People Who Love Gardening
Industry/Entity Type
Publishing
Requirements
Must have
- Title, Subtitle, Author Name, Beautiful Design, Eye Catching making you want to buy the book
Nice to have
- Large title, Easy to read subtitle intriguing pictures
Should not have
- Busy with too much stuff going on

```html
<!DOCTYPE html>
<html lang="en">
<head>
<meta charset="utf-8">
<title>Quiet Hollow Journals – Cover Wrap</title>
<link rel="stylesheet" href="https://fonts.googleapis.com/css2?family=Arimo:wght@400;700&family=Caveat:wght@400&family=Oswald:wght@600;700&display=swap">
<style>
  :root {
    --leaf-dark: #2f4a1c;
    --leaf-mid: #5f7d3a;
    --leaf-light: #9fb07a;
    --haze: #c9cdb4;
    --fruit: #a8322e;
    --band: #437a23;
    --bullet: #6aa23a;
    --ink-light: #ffffff;
    --shadow: rgba(0,0,0,0.75);
  }
  html, body {
    margin: 0;
    padding: 0;
    width: 1200px;
    height: 590px;
    overflow: hidden;
    background: #ececec;
  }
  .cover-wrap {
    position: relative;
    width: 1200px;
    height: 590px;
    overflow: hidden;
    color: var(--ink-light);
  }
  .orchard-photo {
    position: absolute;
    inset: 0;
    background:
      radial-gradient(ellipse at 85% 55%, rgba(168,50,46,0.35), transparent 45%),
      radial-gradient(ellipse at 15% 10%, var(--haze), transparent 40%),
      linear-gradient(160deg, var(--leaf-light) 0%, var(--leaf-mid) 35%, var(--leaf-dark) 75%, var(--leaf-mid) 100%);
  }
  .green-band {
    position: absolute;
    left: 0;
    top: 424px;
    width: 1200px;
    height: 108px;
    background: var(--band);
  }

  /* Back cover */
  .back-cover {
    position: absolute;
    left: 0;
    top: 0;
    width: 600px;
    height: 590px;
  }
  .blurb {
    position: absolute;
    left: 42px;
    top: 28px;
    width: 518px;
    margin: 0;
    font: 700 11.6px/13.2px "Arimo", Arial, sans-serif;
    text-indent: 16px;
    text-shadow: 0 0 2px var(--shadow);
  }
  .discover-lead {
    position: absolute;
    left: 58px;
    top: 146px;
    margin: 0;
    font: 700 11.5px/14px "Arimo", Arial, sans-serif;
    text-shadow: 0 0 2px var(--shadow);
  }
  .benefit-list {
    position: absolute;
    left: 42px;
    top: 171px;
    width: 490px;
    margin: 0;
    padding: 0;
    list-style: none;
    font: 400 11px/12.2px "Arimo", Arial, sans-serif;
    text-shadow: 0 0 2px var(--shadow);
  }
  .benefit-list li {
    text-indent: 16px;
    height: 24.4px;
    overflow: hidden;
    position: relative;
  }
  .benefit-list li::before {
    content: "";
    position: absolute;
    left: 2px;
    top: 4px;
    width: 5px;
    height: 5px;
    border-radius: 50%;
    background: var(--bullet);
  }
  .more {
    position: absolute;
    left: 56px;
    top: 404px;
    margin: 0;
    font: 400 11px/13px "Arimo", Arial, sans-serif;
    text-shadow: 0 0 2px var(--shadow);
  }
  .back-tagline {
    position: absolute;
    left: 85px;
    top: 448px;
    width: 550px;
    margin: 0;
    text-align: center;
    font: 400 27px/27px "Caveat", cursive;
    letter-spacing: 0.3px;
  }

  /* Front cover */
  .front-cover {
    position: absolute;
    left: 685px;
    top: 0;
    width: 560px;
    height: 590px;
    text-align: center;
  }
  .author {
    position: absolute;
    left: 0;
    top: 18px;
    width: 560px;
    margin: 0;
    font: 700 40px/52px "Oswald", sans-serif;
    letter-spacing: 0.5px;
    text-transform: uppercase;
    text-shadow: 2px 2px 3px var(--shadow);
  }
  .subtitle {
    position: absolute;
    left: 0;
    top: 124px;
    width: 560px;
    margin: 0;
    font: 700 18px/27.3px "Arimo", Arial, sans-serif;
    text-shadow: 1px 1px 2px var(--shadow), 0 0 4px var(--shadow);
  }
  .subtitle .lead-step {
    font-size: 28px;
  }
  .title {
    position: absolute;
    left: 0;
    top: 344px;
    width: 560px;
    margin: 0;
  }
  .title-main {
    display: block;
    font: 700 74px/90px "Oswald", sans-serif;
    letter-spacing: 1px;
    text-transform: uppercase;
    text-shadow: 2px 2px 4px rgba(0,0,0,0.4);
  }
  .title-script {
    display: block;
    margin-top: -8px;
    font: 400 104px/104px "Caveat", cursive;
  }
</style>
</head>
<body>
  <main class="cover-wrap">
    <div class="orchard-photo" role="img" aria-label="Soft-focus photograph of an apple orchard with red apples among green leaves"></div>
    <div class="green-band"></div>

    <section class="back-cover">
      <p class="blurb">How to grow a thriving orchard and reap a bountiful harvest in less than a year – in both urban and non-urban settings. Fruit trees are fun to grow and will reward you with years of fresh, juicy homegrown produce. However, the process can be excruciating, especially if you don’t know the best varieties to grow or how to control pests and diseases. With a little planning and guidance, you will soon be biting into mellow fruits from trees in your backyard – including cherries, plums, pears, apples, and more. All you need is to learn how to care for the trees, which you will find inside.</p>
      <p class="discover-lead">In Quiet Hollow Journals, you’ll discover:</p>
      <ul class="benefit-list">
        <li>How to pick the right fruit tree varieties for your growing zone and needs to ensure the plants don’t die</li>
        <li>How to effectively plan and prepare the planting site to lay a good foundation for your incoming trees</li>
        <li>How to choose the right irrigation system for your orchard and keep your fruit trees nourished all year long</li>
        <li>Examples of fruit garden plans for different regions – including a guide to help you design your small backyard space</li>
        <li>How to plant fruits to ensure proper pollination, fertilization, and flourishing growth of your produce</li>
        <li>Different fruit tree propagation methods with step-by-step instructions to help you grow your trees without spending money on costly grafts</li>
        <li>When and how to harvest fruits to ensure you collect them at their best and prevent wasting your hard work</li>
        <li>How to boost fruit production, encourage growth, and protect your trees from dangerous diseases</li>
        <li>How to look after fruit trees during all seasons, practice organic farming, and control pests in your garden</li>
      </ul>
      <p class="more">And much more…</p>
      <p class="back-tagline">It’s time to grow your mini-orchard and bask in<br>years of harvest and sweetness from your labor.</p>
    </section>

    <section class="front-cover">
      <p class="author">Marguerite Olundvale</p>
      <p class="subtitle"><span class="lead-step">9 Simple Steps</span> Including,<br>Site Selection,<br>Pollination and Fertilization,<br>Pruning,<br>Small Spaces,<br>Pest Control,<br>Tropical Fruit Trees, and Berries</p>
      <h1 class="title">
        <span class="title-main">Quiet Hollow</span>
        <span class="title-script">Journals</span>
      </h1>
    </section>
  </main>
</body>
</html>
```